Innovative Consulting Firm Needs New Business Cards and Stationary

Our Innovative Consulting Firm, Harrowgate Consulting, is in need of new business cards and stationary designs. We want two-sided cards that incorporate our logo, which is attached. We are looking for something not too formal, but is professional and slick.

Card should have the following information:
Name (ex. Lena Vork)
Title (ex. Manager)
Address (ex. 24680 Quill Avenue)
Address 2 (ex. Suite 100)
City
State
Zip Code
Mobile
Email

The card should also have our website: www.harrowgateconsulting.example

Industry/Entity Type

Management Consulting

Contact Information for Business Card

Name (ex. Lena Vork)
Title (ex. Manager)
Address 2 (ex. Suite 100)
City
State
Zip Code
Mobile
Email

Font styles to use
Sans Serif

Requirements
Must have
• The colors on the card must match the colors in the logo. The exact color codes are attached in a pdf.
Nice to have
• The Company's Tagline is "Focused on your Future". This might be nice to incorporate, but not necessary.

```html
<!DOCTYPE html>
<html lang="en">
<head>
<meta charset="utf-8">
<title>Harrowgate Consulting – Business Cards</title>
<link rel="stylesheet" href="https://fonts.googleapis.com/css2?family=Montserrat:wght@500;600;700&family=Michroma&display=swap">
<style>
  :root {
    --navy: #1f5a8c;
    --gold: #f4b21c;
    --white: #ffffff;
    --backdrop: #e9ebee;
    --ink: #1f4f7e;
  }
  * { box-sizing: border-box; margin: 0; padding: 0; }
  html, body { width: 1200px; height: 900px; overflow: hidden; }
  body {
    background: var(--backdrop);
    font-family: "Montserrat", Arial, sans-serif;
    position: relative;
  }
  .card {
    position: absolute;
    left: 250px;
    width: 700px;
    height: 400px;
    background: var(--white);
    border-radius: 34px;
    overflow: hidden;
    box-shadow: 0 6px 18px rgba(0,0,0,0.12);
  }
  .card--front { top: 35px; }
  .card--back { top: 465px; }

  .wordmark {
    position: absolute;
    color: var(--navy);
    font-weight: 700;
    display: flex;
    align-items: center;
    gap: 14px;
  }
  .wordmark__dot {
    width: 22px; height: 22px;
    background: var(--gold);
    flex: none;
  }
  .wordmark__text { display: flex; flex-direction: column; line-height: 1; }
  .wordmark__name { font-size: 46px; letter-spacing: 0.5px; }
  .wordmark__sub {
    font-size: 14px;
    font-weight: 500;
    letter-spacing: 7px;
    margin-top: 6px;
    text-align: right;
  }
  .card--front .wordmark { left: 205px; top: 140px; }

  .website {
    position: absolute;
    left: 0; right: 0; bottom: 58px;
    text-align: center;
    color: var(--navy);
    font-size: 16px;
    font-weight: 600;
  }
  .website::before, .website::after {
    content: "";
    display: inline-block;
    width: 6px; height: 6px;
    border-radius: 50%;
    background: var(--gold);
    vertical-align: middle;
    margin: 0 8px;
  }

  .swoosh { position: absolute; inset: 0; }
  .card--back .wordmark { left: 48px; top: 72px; }
  .card--back .wordmark__name { font-size: 38px; }
  .card--back .wordmark__sub { font-size: 12px; letter-spacing: 6px; }
  .card--back .wordmark__dot { width: 18px; height: 18px; }

  .tagline {
    position: absolute;
    left: 50px; top: 200px;
    font-family: "Michroma", Arial, sans-serif;
    font-size: 13px;
    color: var(--ink);
    letter-spacing: 0.3px;
  }
  .contact {
    position: absolute;
    right: 36px; top: 92px;
    text-align: right;
    color: var(--white);
  }
  .contact__name {
    color: var(--gold);
    font-size: 22px;
    font-weight: 600;
    letter-spacing: 0.5px;
    line-height: 1.2;
  }
  .contact__title { font-size: 13px; margin-bottom: 30px; }
  .contact__list { list-style: none; font-size: 12.5px; line-height: 1.75; font-weight: 500; }
  .contact__list li { display: flex; justify-content: flex-end; align-items: center; gap: 9px; }
  .contact__list svg { width: 12px; height: 12px; flex: none; }
</style>
</head>
<body>
  <section class="card card--front">
    <div class="wordmark">
      <span class="wordmark__dot"></span>
      <span class="wordmark__text">
        <span class="wordmark__name">Harrowgate</span>
        <span class="wordmark__sub">CONSULTING</span>
      </span>
    </div>
    <p class="website">www.harrowgateconsulting.example</p>
  </section>

  <section class="card card--back">
    <svg class="swoosh" viewBox="0 0 700 400" aria-hidden="true">
      <path d="M0,385 C180,380 330,330 510,0 L700,0 L700,400 L0,400 Z" fill="var(--navy)"/>
      <path d="M0,358 C165,354 310,306 490,0 L499,0 C322,316 172,368 0,374 Z" fill="var(--gold)"/>
    </svg>
    <div class="wordmark">
      <span class="wordmark__dot"></span>
      <span class="wordmark__text">
        <span class="wordmark__name">Harrowgate</span>
        <span class="wordmark__sub">CONSULTING</span>
      </span>
    </div>
    <p class="tagline">FOCUSED ON YOUR FUTURE</p>
    <div class="contact">
      <p class="contact__name">LENA VORK</p>
      <p class="contact__title">Manager</p>
      <ul class="contact__list">
        <li>+330 555-0142
          <svg viewBox="0 0 12 12"><rect x="3" y="0.5" width="6" height="11" rx="1.2" fill="none" stroke="var(--gold)" stroke-width="1.3"/></svg></li>
        <li>info@harrowgateconsulting.example
          <svg viewBox="0 0 12 12"><rect x="0.7" y="2" width="10.6" height="8" fill="none" stroke="var(--gold)" stroke-width="1.3"/><path d="M1,2.5 L6,6.5 L11,2.5" fill="none" stroke="var(--gold)" stroke-width="1.2"/></svg></li>
        <li>www.harrowgateconsulting.example
          <svg viewBox="0 0 12 12"><circle cx="6" cy="6" r="5.3" fill="none" stroke="var(--gold)" stroke-width="1.2"/><path d="M0.7,6 H11.3 M6,0.7 C3,4 3,8 6,11.3 M6,0.7 C9,4 9,8 6,11.3" fill="none" stroke="var(--gold)" stroke-width="1"/></svg></li>
        <li>24680 Quill Avenue Suite 100
          <svg viewBox="0 0 12 12"><path d="M6,11.5 C2.5,7 2,5.5 2,4.2 A4,4 0 0 1 10,4.2 C10,5.5 9.5,7 6,11.5 Z" fill="var(--gold)"/><circle cx="6" cy="4.2" r="1.4" fill="var(--navy)"/></svg></li>
      </ul>
    </div>
  </section>
</body>
</html>
```